Ferlane Capital, a private equity fund, needs a brochure

Ferlane Capital is a private equity fund dedicated to the development of budget hotels in France (reasonably priced hotel rooms).
Our customers are French private and high-income investors.

The brochure should communicate :
- seriousness and expertise
- trust, confidence and security
- financial product and profitability

The title is : Investissez dans l'hôtellerie économique et l'immobilier

Brochure size :
3 pages A4
Open size : 63 x 29,7 cm
Closed size : 21 x 29,7 cm

Our competitors :
Brivento http://brivento-immo-example.fr/
789 Ventara http://www.789ventara-example.com/
LMR Capital http://www.lmrex-example.com/
Solvio capital http://www.solviocapital-example.fr/
Dravomont http://www.dravomont-example.fr/

Target Market(s)

Private investors, high-income ; Institutional investors ; Target customers are French private investors with high revenue.

Industry/Entity Type

Financial

Requirements
Must have
• - Brochure must respect our identity (you can see our logo) and use its colors and typo (and/or same typo style)
- You must use pictures on each interior pages (pictures of projetc and hotels)

```html
<!DOCTYPE html>
<html lang="fr">
<head>
<meta charset="utf-8">
<title>Ferlane Capital – Brochure</title>
<link href="https://fonts.googleapis.com/css2?family=Tinos:ital,wght@0,400;0,700;1,400&display=swap" rel="stylesheet">
<style>
:root{
  --red:#b3172b;
  --red-dark:#9a1224;
  --grey-dark:#4a4a4c;
  --grey-mid:#6f6f71;
  --grey-light:#bdbdbf;
  --panel:#e6e6e8;
  --text:#4d4d4f;
  --paper:#ffffff;
}
*{margin:0;padding:0;box-sizing:border-box}
html,body{width:1200px;height:566px;overflow:hidden;background:var(--paper)}
body{font-family:"Tinos",serif;color:var(--text);position:relative}
.abs{position:absolute}
p,li{font-size:6.6px;line-height:1.22}
ul{list-style:none}
li{padding-left:6px;position:relative}
li::before{content:"•";position:absolute;left:0;color:var(--red)}
.title{color:var(--red);font-weight:400;font-size:12.5px;letter-spacing:.3px;text-transform:uppercase}
.heading{color:var(--red);font-weight:400;font-size:9px;line-height:1.15;text-transform:uppercase;margin-bottom:6px}
.heading-light{color:#fff}
.photo{position:absolute}
.fold{position:absolute;top:0;height:566px;border-left:1px dashed #777}
/* left page */
.band-red{left:0;top:97px;width:312px;height:56px;background:var(--red);padding:8px 22px 0 30px}
.band-red p{color:#fff;font-size:8.6px;line-height:1.15;text-transform:uppercase}
.band-quote{left:0;top:229px;width:312px;height:85px;background:var(--grey-dark)}
.quote{position:absolute;right:96px;top:10px;width:190px;text-align:right;color:#fff;font-style:italic;font-size:14px;line-height:1.2}
/* middle */
.panel-mid{left:477px;top:40px;width:317px;height:71px;background:var(--panel)}
.band-dark{left:477px;top:111px;width:317px;height:149px;background:var(--grey-mid);padding:10px 18px;color:#fff}
.band-dark p,.band-dark li{color:#fff}
.panel-focus{left:477px;top:384px;width:317px;height:146px;background:var(--panel)}
/* right */
.chip{position:absolute;top:197px;height:28px;width:110px;display:flex;align-items:center;justify-content:center;text-align:center;color:#fff;font-size:7.4px;line-height:1.1;text-transform:uppercase}
.schema{left:822px;top:250px;width:348px;text-align:center;font-weight:700;font-size:10.5px;color:#222}
</style>
</head>
<body>

<!-- LEFT PAGE -->
<section class="abs" style="left:30px;top:34px;width:270px">
  <h1 class="title">Un véhicule innovant</h1>
  <p style="margin-top:12px">Ferlane Capital (Hôtels Ferlane) est une société d'investissement constituée sous la forme d'une SAS à capital variable ayant opté pour le régime fiscal des sociétés de capital-risque (« SCR »).</p>
</section>

<div class="abs band-red"><p>Les société de capital-risque bénéficient d'un régime fiscal de faveur prévu par la loi n° 85-695 du 11 juillet 1985 et les dispositions légales et réglementaires du code général des impôts.</p></div>

<section class="abs" style="left:30px;top:162px;width:262px">
  <p>Les associés personnes physiques peuvent bénéficier d'un régime d'exonération d'impôt sur le revenu pour les dividendes perçus et les plus-values de cession de titres réalisées (seules les contributions sociales restant applicables) à condition notamment de conserver les actions et de réinvestir leurs produits dans la SCR pendant une durée de 5 ans.</p>
  <p>Les conditions d'application de ce régime sont présentées à titre indicatif et de manière synthétique dans un document annexe auquel il convient de se reporter.</p>
</section>

<div class="abs band-quote">
  <p class="quote">“Nous nous positionnons sur des marchés en croissance qui ont prouvé leur résistance face à la crise.”</p>
  <div class="photo" role="img" aria-label="Portrait du dirigeant" style="left:222px;top:6px;width:62px;height:78px;background:linear-gradient(160deg,#8a8f99,#3f4450)"></div>
</div>

<section class="abs" style="left:30px;top:326px;width:262px">
  <h2 class="heading">Une société de capital-risque conçue et gérée par le groupe Kelvar Outremer</h2>
  <p>Fort d'une connaissance approfondie en ingénierie financière et en promotion immobilière, le Groupe Kelvar Outremer et ses filiales bénéficient d'une expérience de plus de vingt ans dans la structuration financière, juridique et fiscale d'investissements immobiliers et industriels.</p>
  <ul style="width:180px">
    <li>4000 projets structurés et financés depuis vingt ans.</li>
    <li>3000 investisseurs satisfaits.</li>
    <li>800 sociétés sous gestion.</li>
  </ul>
</section>

<section class="abs" style="left:30px;top:426px;width:190px">
  <h2 class="heading">Des investissements centrés sur l'hôtellerie et l'immobilier</h2>
  <p>Ferlane Capital a pour objectif d'accueillir jusqu'à 30 millions d'euro de souscriptions sur 2 ans. Le produit de ces souscriptions permettra la prise de participations minoritaires (40% maximum) dans le capital de sociétés ayant pour objet :</p>
  <ul>
    <li>La construction ou l'acquisition d'hôtels économiques et leur exploitation.</li>
    <li>La construction ou l'acquisition de meublés de tourisme et leur exploitation.</li>
    <li>La construction-vente d'immeuble en VEFA.</li>
  </ul>
</section>

<div class="photo" role="img" aria-label="Chambre d'hôtel" style="left:222px;top:392px;width:81px;height:82px;background:linear-gradient(135deg,#c9b08a,#7a5e3f)"></div>
<div class="photo" role="img" aria-label="Salle de réunion d'hôtel" style="left:222px;top:484px;width:81px;height:78px;background:linear-gradient(135deg,#b99c72,#6c5a45)"></div>

<!-- PHOTO STRIP -->
<div class="photo" role="img" aria-label="Accueil d'un hôtel économique" style="left:312px;top:0;width:164px;height:178px;background:linear-gradient(170deg,#c7c1b9 0%,#b9412f 55%,#e0d9cf 100%)"></div>
<div class="photo" role="img" aria-label="Façade d'hôtel avec terrasse" style="left:312px;top:187px;width:164px;height:192px;background:linear-gradient(180deg,#a9c2d6 0%,#9a6d4a 50%,#5a5a5a 100%)"></div>
<div class="photo" role="img" aria-label="Façade vitrée d'immeuble" style="left:312px;top:388px;width:164px;height:178px;background:linear-gradient(160deg,#2f5f8e,#9fb9cf 60%,#3b4f63)"></div>
<div class="fold" style="left:396px"></div>

<!-- MIDDLE PAGE -->
<div class="photo" role="img" aria-label="Perspective d'un projet hôtelier tropical" style="left:477px;top:0;width:317px;height:40px;background:linear-gradient(90deg,#7e9c6a,#c9d3c0 50%,#6d8b5c)"></div>
<div class="abs panel-mid"></div>
<section class="abs" style="left:495px;top:25px;width:282px">
  <p>L'activité de Ferlane Capital est notamment centrée sur l'investissement dans des sociétés développant une activité commerciale d'exploitation d'hôtels économiques. Ces sociétés du portefeuille seront à terme propriétaires des actifs immobiliers qu'elles exploitent.</p>
  <p>Ferlane Capital pourra également diversifier ses investissements dans les secteurs de la promotion immobilière et de l'immobilier de service (meublés de tourisme et/ou résidences médicalisées).</p>
</section>

<section class="abs band-dark">
  <h2 class="heading heading-light">Pourquoi l'hôtellerie et l'immobilier ?</h2>
  <p>Dans des conditions économiques et financières perturbées depuis la crise financière de 2008, les investisseurs exigent aujourd'hui des placements structurés pour résister aux effets économiques induits. Selon l'analyse des équipes de Ferlane Capital, le marché de l'hôtellerie économique en croissance depuis sa création répond particulièrement bien à ces attentes. Ce positionnement est en adéquation avec la baisse des budgets alloués aux déplacements et voyages professionnels et touristiques.</p>
  <p>Le marché de l'immobilier reste quant à lui une valeur refuge en temps de crise, selon l'analyse des équipes de Ferlane Capital :</p>
  <ul>
    <li>Un marché en croissance malgré la crise.</li>
    <li>Sur 2011, la croissance cumulée du nombre de nuitées atteint + 3,2% par rapport à 2010. (<i>source Vantia</i>).</li>
    <li>Secteur porteur. 1,5 milliard d'euros ont été investis dans le secteur de l'hôtellerie en France en 2011. (<i>source Vantia</i>).</li>
  </ul>
</section>

<section class="abs" style="left:495px;top:270px;width:282px">
  <h2 class="heading">Un partenariat avec Meridel Hotels Group</h2>
  <p>Pour l'exploitation des investissements hôteliers, les sociétés du portefeuille interviendront en partenariat avec un opérateur hôtelier – MERIDEL HOTELS GROUP – dans le cadre d'un accord de franchise (Meridel Hotels Group, 2ème opérateur d'Europe, plus de 1000 hôtels dans le monde).</p>
  <ul>
    <li>Contrats de franchise sous enseignes : Étape Une **, Clairval *** et Iris Inn ***.</li>
    <li>Contrats d'assistante technique.</li>
    <li>Implantation de plus de 12 hôtels dans 6 régions françaises d'outremer.</li>
  </ul>
  <h2 class="heading" style="margin-top:8px">Focus sur l'hôtellerie économique<br>dans les régions françaises ultramarines</h2>
</section>

<div class="abs panel-focus"></div>
<section class="abs" style="left:495px;top:390px;width:282px">
  <p>Le marché des hôtels économiques normés et standardisés sous une enseigne nationale ou internationale est peu développé dans les DOM-COM. Ces régions sont équipées principalement d'hôtels balnéaires à vocation touristique essentiellement implantés sur des lieux généralement éloignés des centres économiques. Depuis une vingtaine d'années, le développement important des populations et la centralisation des zones commerciales et industrielles sur les capitales administratives ont généré d'importants embouteillages qui compliquent les accès à ces zones. L'offre hôtelière n'est plus en adéquation avec les attentes des visiteurs professionnels. La création d'une chaîne d'hôtels économiques est la réponse à ce besoin et bénéficie de l'appui de la puissance publique et des instances régionales.</p>
  <ul>
    <li>Absence d'hôtels économiques standardisés et normés dans ces régions.</li>
    <li>Structures hôtelières existantes inadaptées aux besoins du marché professionnel et coûteuses : prix des nuitées proposées par ces nouveaux hôtels inférieurs de 30 à 50% aux prix pratiqués localement.</li>
    <li>Programmes d'investissements bénéficiant d'avantages fiscaux, sociaux et de subventions.</li>
  </ul>
</section>
<div class="photo" role="img" aria-label="Perspective d'un projet immobilier" style="left:477px;top:530px;width:317px;height:36px;background:linear-gradient(90deg,#c8d2da,#8fa3b3 50%,#d7dde2)"></div>
<div class="fold" style="left:794px"></div>

<!-- RIGHT PAGE -->
<section class="abs" style="left:822px;top:36px;width:348px">
  <h2 class="heading" style="margin-bottom:4px">Immobilier, valeur refuge pour l'investisseur<br>(selon l'analyse de Ferlane Capital)</h2>
  <ul>
    <li>Un investissement dans la pierre.</li>
    <li>Une réponse à l'incertitude des marchés financiers et de la monnaie et des risques d'inflation.</li>
    <li>Des emplacements exceptionnels (centres villes, aéroports, zones commerciales).</li>
  </ul>
  <h2 class="heading" style="margin-top:10px">Trois sources potentielles de gains</h2>
  <p>Une double plus-value potentielle hôtelière et immobilière assortie d'un rendement annuel. La création de valeur pour chacun des hôtels dans lesquels Ferlane Capital prendra des participations proviendra de la valorisation des murs de l'hôtel, de la valorisation de son fonds de commerce et de la rentabilité annuelle de l'exploitation. L'activité de location de meublés de tourisme bénéficie des mêmes synergies. La création de valeur pour l'activité de promotion immobilière (construction vente des immeubles) proviendra des marges dégagées par les opérations de promotion</p>
  <ul>
    <li>Trois sources potentielles de gains, assorties toutefois d'un risque de perte en capital</li>
    <li>Atténuation de risques du fait de l'investissement diversifié dans les murs et dans le fonds de commerce</li>
    <li>Un recours à un financement peu coûteux</li>
  </ul>
</section>

<div class="chip" style="left:822px;background:var(--grey-dark)">Plus-values hôtelières</div>
<div class="chip" style="left:936px;background:var(--grey-mid)">Plus-values immobilières</div>
<div class="chip" style="left:1051px;background:var(--grey-light)">Rendement annuel capitalisé</div>

<p class="abs schema">SCHEMA à FAIRE</p>

<section class="abs" style="left:822px;top:306px;width:348px">
  <h2 class="heading">Comment sont répartis les gains ?</h2>
  <p>Le capital de la société Ferlane Capital est constitué de deux types de catégorie d'actions A et B.</p>
  <ul>
    <li>Les actions de type A destinées aux investisseurs.</li>
    <li>Les actions de type B (carried-interest) destinées à être souscrites par les personnes intervenant dans la gestion de Ferlane Capital</li>
    <li>En vertu des dispositions légales et statutaires applicables, l'émission de 100 actions de type A oblige à émettre 1 action B. Ne pouvant être souscrite que par les personnes intervenant dans la gestion de Ferlane Capital.</li>
  </ul>
  <p>Les droits préférentiels attachés aux actions A et aux actions B sont définis à l'article 14.2 des statuts de Ferlane Capital et répondent notamment au principe selon lequel l'actif net de liquidation au-delà d'un “rendement” de 7% l'an sera répartis à hauteur de 80% pour les actions A (investisseurs) et 20% pour les actions B (personnes intervenant dans la gestion du fonds).</p>
</section>

<div class="photo" role="img" aria-label="Chambre d'hôtel orange" style="left:822px;top:430px;width:106px;height:56px;background:linear-gradient(135deg,#e6a14a,#8a5a2c)"></div>
<div class="photo" role="img" aria-label="Salle de petit-déjeuner" style="left:936px;top:430px;width:107px;height:56px;background:linear-gradient(135deg,#e8e2dc,#c6463a)"></div>
<div class="photo" role="img" aria-label="Espace d'accueil coloré" style="left:1051px;top:430px;width:110px;height:56px;background:linear-gradient(135deg,#f0c05a,#c8612f)"></div>
<div class="photo" role="img" aria-label="Chambre d'hôtel claire" style="left:822px;top:492px;width:106px;height:56px;background:linear-gradient(135deg,#cfc7bb,#6f7a5b)"></div>
<div class="photo" role="img" aria-label="Restaurant d'hôtel" style="left:936px;top:492px;width:107px;height:56px;background:linear-gradient(135deg,#b98a5c,#5a3b2a)"></div>
<div class="photo" role="img" aria-label="Chambre d'hôtel verte" style="left:1051px;top:492px;width:110px;height:56px;background:linear-gradient(135deg,#c9d36a,#7b5a36)"></div>

</body>
</html>
```